Android App Design Project

Hi my name is Keril, and I'm an android developer. I'm searching for a professional designer that can design my app.I have already launched the app and you can find it in the appora depot.

Main Requirements
- 15 sport icons
- 6 android pages
- Action bar
- Buttons and other icons

You need to do all requirements to submit a design. I need the design in both JPEG format and Photoshop PSD format. If you are interested then please download the PDF file ,it will help you a lot.
The name of the app is "MATCH VUE Prime" you can find it in Appora Shelf.

NOTICE: You might read that the Payment is not guaranteed if I'm not happy with the design BUT if you make a good design and you win the contest, then you become my main designer that means if I want to change or add something to the design of the app in the future I return to you "the winner" directly to make the redesign and get paid for it.

Regards.
Skype: Idun marvelo "idun47"
E-mail: idunkeril@mailvox.test

Industry/Entity Type

Tv

Requirements
Must have
• - 15 sport icons
- 6 android pages
- Action bar
- Buttons and other icons

```html
<!DOCTYPE html>
<html lang="en">
<head>
<meta charset="utf-8">
<title>Tennis – Match List</title>
<link href="https://fonts.googleapis.com/css2?family=Roboto:wght@400;500&display=swap" rel="stylesheet">
<style>
:root{
  --status-bg:#000;
  --status-accent:#33b5e5;
  --bar-top:#6ec3ee;
  --bar-bottom:#2a8ccb;
  --bar-divider:#1f6fa3;
  --bar-ink:#0c0c0c;
  --icon-ink:#1d5f88;
  --screen-bg:#0c2430;
  --row-line:#5b6b73;
  --title-ink:#ffffff;
  --live-ink:#f2cf2a;
  --ad-blue:#2f8fd2;
  --ad-gold:#b67c06;
  --ad-ink:#1c4d73;
  --nav-bg:#000;
  --nav-ink:#9a9a9a;
  --badge:#e8820e;
  --mark-fill:#ffffff;
}
*{margin:0;padding:0;box-sizing:border-box}
html,body{width:675px;height:1200px;overflow:hidden;background:var(--screen-bg)}
body{font-family:"Roboto",sans-serif;position:relative}
.status-bar{position:absolute;top:0;left:0;width:675px;height:47px;background:var(--status-bg)}
.status-bar .clock-text{position:absolute;right:12px;top:6px;color:var(--status-accent);font-size:29px}
.status-bar svg{position:absolute;top:8px}
.action-bar{position:absolute;top:47px;left:0;width:675px;height:91px;
  background:linear-gradient(var(--bar-top),var(--bar-bottom));border-bottom:1px solid #8fb9cf}
.action-bar .title{position:absolute;left:81px;top:22px;font-size:34px;color:var(--bar-ink)}
.action-bar .up{position:absolute;left:8px;top:33px}
.action-bar .app-mark{position:absolute;left:26px;top:23px;width:46px;height:46px;border-radius:50%;background:var(--mark-fill)}
.action-btn{position:absolute;top:0;height:91px;width:103px;border-left:1px solid var(--bar-divider);
  display:flex;align-items:center;justify-content:center}
.match-list{position:absolute;top:138px;left:0;width:675px;height:882px;overflow:hidden;list-style:none}
.match{position:relative;height:129px;border-bottom:2px solid var(--row-line);margin:0 38px 0 34px}
.match .teams{position:absolute;left:16px;top:26px;font-size:36px;color:var(--title-ink)}
.match .meta{position:absolute;left:16px;top:72px;display:flex;align-items:center;font-size:27px;color:var(--title-ink)}
.match .live{color:var(--live-ink);font-weight:500;font-size:25px;width:116px}
.match .time{display:flex;align-items:center;gap:5px}
.ad-banner{position:absolute;top:1020px;left:0;width:675px;height:89px;
  background:linear-gradient(var(--ad-blue) 0%,#fff 50%,var(--ad-gold) 52%,#f2c55a 75%,#fff 100%)}
.ad-banner span{position:absolute;left:50px;top:8px;font-size:34px;color:var(--ad-ink)}
.nav-bar{position:absolute;top:1109px;left:0;width:675px;height:91px;background:var(--nav-bg)}
.nav-bar svg{position:absolute;top:28px}
</style>
</head>
<body>
<header class="status-bar">
  <svg style="left:472px" width="26" height="30" viewBox="0 0 26 30"><path d="M4 11h5l7-6v20l-7-6H4z" fill="none" stroke="#8a8a8a" stroke-width="2"/><line x1="2" y1="27" x2="24" y2="3" stroke="#8a8a8a" stroke-width="2"/></svg>
  <svg style="left:508px" width="38" height="32" viewBox="0 0 38 32"><text x="2" y="10" font-size="11" fill="#bbb" font-family="Roboto,sans-serif">H</text><path d="M4 30h4v-6H4zM11 30h4v-11h-4zM18 30h4v-16h-4zM25 30h4v-22h-4z" fill="var(--status-accent)"/></svg>
  <svg style="left:555px" width="20" height="32" viewBox="0 0 20 32"><rect x="6" y="0" width="8" height="3" fill="var(--status-accent)"/><rect x="1" y="3" width="18" height="28" fill="var(--status-accent)"/></svg>
  <span class="clock-text">10:07</span>
</header>

<nav class="action-bar">
  <svg class="up" width="12" height="22" viewBox="0 0 12 22"><path d="M10 2 3 11l7 9" fill="none" stroke="var(--bar-ink)" stroke-width="2.5"/></svg>
  <span class="app-mark" aria-hidden="true"></span>
  <span class="title">Tennis</span>
  <div class="action-btn" style="left:366px">
    <svg width="48" height="48" viewBox="0 0 48 48"><path d="M8 22A16 16 0 0 1 37 13" fill="none" stroke="var(--icon-ink)" stroke-width="5"/><path d="M40 4v12H28z" fill="var(--icon-ink)"/><path d="M40 26A16 16 0 0 1 11 35" fill="none" stroke="var(--icon-ink)" stroke-width="5"/><path d="M8 44V32h12z" fill="var(--icon-ink)"/></svg>
  </div>
  <div class="action-btn" style="left:469px">
    <svg width="72" height="52" viewBox="0 0 72 52"><path d="M4 6h62v34H30l-8 10v-10H4z" fill="#154a6e" stroke="#0f3a57" stroke-width="1.5"/><circle cx="64" cy="6" r="6" fill="var(--badge)" stroke="#fff" stroke-width="1"/><text x="64" y="9" font-size="8" text-anchor="middle" fill="#fff" font-family="Roboto,sans-serif">7</text></svg>
  </div>
  <div class="action-btn" style="left:572px">
    <svg width="50" height="50" viewBox="0 0 50 50"><circle cx="25" cy="25" r="22" fill="none" stroke="var(--icon-ink)" stroke-width="3"/><circle cx="25" cy="14" r="3" fill="var(--icon-ink)"/><rect x="22" y="21" width="6" height="18" fill="var(--icon-ink)"/></svg>
  </div>
</nav>

<ul class="match-list">
  <li class="match"><span class="teams">Team1 vs. Team2</span><div class="meta"><span class="live">Live!</span><span class="time"><svg width="27" height="27" viewBox="0 0 28 28"><circle cx="14" cy="14" r="12" fill="none" stroke="#fff" stroke-width="2"/><path d="M14 6v8l-4 5" fill="none" stroke="#fff" stroke-width="2"/></svg>21:00</span></div></li>
  <li class="match"><span class="teams">Team1 vs. Team2</span><div class="meta"><span class="time"><svg width="27" height="27" viewBox="0 0 28 28"><circle cx="14" cy="14" r="12" fill="none" stroke="#fff" stroke-width="2"/><path d="M14 6v8l-4 5" fill="none" stroke="#fff" stroke-width="2"/></svg>11:00</span></div></li>
  <li class="match"><span class="teams">Team1 vs. Team2</span><div class="meta"><span class="time"><svg width="27" height="27" viewBox="0 0 28 28"><circle cx="14" cy="14" r="12" fill="none" stroke="#fff" stroke-width="2"/><path d="M14 6v8l-4 5" fill="none" stroke="#fff" stroke-width="2"/></svg>21:00</span></div></li>
  <li class="match"><span class="teams">Team1 vs. Team2</span><div class="meta"><span class="live">Live!</span><span class="time"><svg width="27" height="27" viewBox="0 0 28 28"><circle cx="14" cy="14" r="12" fill="none" stroke="#fff" stroke-width="2"/><path d="M14 6v8l-4 5" fill="none" stroke="#fff" stroke-width="2"/></svg>21:00</span></div></li>
  <li class="match"><span class="teams">Team1 vs. Team2</span><div class="meta"><span class="live">Live!</span><span class="time"><svg width="27" height="27" viewBox="0 0 28 28"><circle cx="14" cy="14" r="12" fill="none" stroke="#fff" stroke-width="2"/><path d="M14 6v8l-4 5" fill="none" stroke="#fff" stroke-width="2"/></svg>21:00</span></div></li>
  <li class="match"><span class="teams">Team1 vs. Team2</span><div class="meta"><span class="live">Live!</span><span class="time"><svg width="27" height="27" viewBox="0 0 28 28"><circle cx="14" cy="14" r="12" fill="none" stroke="#fff" stroke-width="2"/><path d="M14 6v8l-4 5" fill="none" stroke="#fff" stroke-width="2"/></svg>21:00</span></div></li>
  <li class="match"><span class="teams">Team1 vs. Team2</span><div class="meta"><span class="live">Live!</span><span class="time"><svg width="27" height="27" viewBox="0 0 28 28"><circle cx="14" cy="14" r="12" fill="none" stroke="#fff" stroke-width="2"/><path d="M14 6v8l-4 5" fill="none" stroke="#fff" stroke-width="2"/></svg>21:00</span></div></li>
</ul>

<aside class="ad-banner"><span>AD Banner Placeholder</span></aside>

<footer class="nav-bar">
  <svg style="left:118px" width="64" height="34" viewBox="0 0 64 34"><path d="M14 4 4 12l10 8M4 12h44a10 10 0 0 1 0 20H20" fill="none" stroke="var(--nav-ink)" stroke-width="3"/></svg>
  <svg style="left:302px" width="70" height="36" viewBox="0 0 70 36"><path d="M2 14 35 2l33 12v20H2z" fill="none" stroke="var(--nav-ink)" stroke-width="3"/></svg>
  <svg style="left:494px" width="66" height="36" viewBox="0 0 66 36"><rect x="2" y="14" width="50" height="20" fill="none" stroke="var(--nav-ink)" stroke-width="3"/><path d="M10 8h48v18" fill="none" stroke="var(--nav-ink)" stroke-width="3"/></svg>
</footer>
</body>
</html>
```